Motorcycle Shop Business Card

New business card for Motorcycle repair and customization shop.Business name: Copper Falcon Chris Morris443-865-5190, 7214 Quarry Lane Ashcombe, MD 21990. www.dale@copperfalconcustoms.example. I uploaded some motorcycle images and logo and a couple of our calendar shoots. They do not have to be used on card just examples of some of our work and past graphic work.
We work on Vantor Brennick and Custom Built Motorcycles.

Looking for front and back design

Target Market(s)

Motorcycle owners

Industry/Entity Type

Motorcycle Part

```html
<!DOCTYPE html>
<html lang="en">
<head>
<meta charset="utf-8">
<title>Copper Falcon Customs – Business Card</title>
<link rel="stylesheet" href="https://fonts.googleapis.com/css2?family=Arimo:wght@400;700&display=swap">
<style>
  :root {
    --backdrop: #8b7356;
    --card-white: #ffffff;
    --card-grey: #eeeeee;
    --photo-light: #f1f1f1;
    --photo-mid: #d9d9d9;
    --ink: #111111;
    --ink-soft: #2a2a2a;
    --rule: #555555;
    --ghost: rgba(255,255,255,0.9);
  }
  * { box-sizing: border-box; margin: 0; padding: 0; }
  html, body {
    width: 1200px; height: 880px; overflow: hidden;
    background: var(--backdrop);
    font-family: "Arimo", Arial, sans-serif;
  }
  .canvas { position: relative; width: 1200px; height: 880px; }

  .card {
    position: absolute;
    width: 560px; height: 320px;
    box-shadow: 0 6px 18px rgba(0,0,0,0.35);
    overflow: hidden;
  }
  .card--front { left: 70px; top: 90px; background: var(--card-white); }
  .card--back  { left: 570px; top: 470px; background: var(--card-grey); }

  .brand-name {
    font-family: "Arimo", Arial, sans-serif;
    font-weight: 700;
    color: var(--ink);
    line-height: 1.05;
    text-align: center;
    letter-spacing: 0.5px;
  }
  .card--front .brand-name {
    position: absolute; left: 0; right: 0; top: 50%;
    transform: translateY(-50%);
    font-size: 44px;
  }

  .shop-photo {
    position: absolute; inset: 0;
    background: linear-gradient(135deg, var(--photo-light) 0%, var(--photo-mid) 45%, var(--photo-light) 100%);
  }
  .card--back .brand-name {
    position: absolute; left: 30px; top: 128px; width: 220px;
    font-size: 32px;
  }
  .divider {
    position: absolute; left: 268px; top: 98px;
    width: 1px; height: 118px; background: var(--rule);
  }
  .contact {
    position: absolute; left: 286px; top: 96px; right: 14px;
    color: var(--ink-soft); font-size: 12.5px; line-height: 1.45;
    white-space: nowrap;
  }
  .contact__name { font-weight: 700; font-size: 19px; color: var(--ink); margin-bottom: 6px; }
  .contact__row { display: flex; align-items: center; gap: 6px; }
  .contact__row svg { width: 13px; height: 13px; flex: none; }
  .contact__rows { margin-top: 8px; }

  .brand-ghost {
    position: absolute; right: 22px; bottom: 34px;
    font-weight: 700; font-size: 18px; color: var(--ghost);
    text-align: center; line-height: 1.05;
  }
</style>
</head>
<body>
<main class="canvas">

  <section class="card card--front" aria-label="Card front">
    <p class="brand-name">Copper Falcon<br>Customs</p>
  </section>

  <section class="card card--back" aria-label="Card back">
    <div class="shop-photo" role="img" aria-label="Faded black and white photo of a custom motorcycle in the workshop"></div>

    <p class="brand-name">Copper Falcon<br>Customs</p>
    <div class="divider"></div>

    <div class="contact">
      <p class="contact__name">Dale Fenwick</p>
      <p>Quarry Lane Ashcombe</p>
      <p>MD 21990</p>
      <div class="contact__rows">
        <p class="contact__row">
          <svg viewBox="0 0 16 16" aria-hidden="true"><circle cx="8" cy="8" r="8" fill="#111"/><path d="M5.2 4.2l1.4-.3.8 2-1 .8c.5 1.1 1.3 1.9 2.4 2.4l.8-1 2 .8-.3 1.4c-3.3.3-6.4-2.8-6.1-6.1z" fill="#fff"/></svg>
          410-555-0137, 7214
        </p>
        <p class="contact__row">
          <svg viewBox="0 0 16 16" aria-hidden="true"><circle cx="8" cy="8" r="8" fill="#111"/><rect x="4" y="5" width="8" height="6" fill="#fff"/><path d="M4 5l4 3.2L12 5" stroke="#111" stroke-width="1" fill="none"/></svg>
          www.dale@copperfalconcustoms.example
        </p>
      </div>
    </div>

    <p class="brand-ghost">Copper Falcon<br>Customs</p>
  </section>

</main>
</body>
</html>
```